Therapist website

I need a sqaure space web design for my therapy practice. I need a home page, a services page with 4 subpages, an about me, an insurnace page, a contact page, an EMDR page

```html
<!DOCTYPE html>
<html lang="en">
<head>
<meta charset="utf-8">
<title>Willowmere Family Counseling</title>
<link rel="stylesheet" href="https://fonts.googleapis.com/css2?family=Lato:wght@400;700;900&family=Great+Vibes&display=swap">
<style>
:root{
  --teal:#4fc1c6;
  --teal-head:#3bb3b9;
  --teal-dark:#17847f;
  --teal-pale:#d3eaeb;
  --paper:#f4f4f4;
  --ink:#444;
  --ink-soft:#666;
  --brown:#b08c6c;
  --footer:#a7a7a7;
  --footer-dark:#5b5b5b;
  --white:#fff;
}
*{box-sizing:border-box;margin:0;padding:0}
html,body{width:1200px;height:3035px;overflow:hidden}
body{position:relative;font-family:"Lato",Arial,sans-serif;color:var(--ink);background:var(--paper)}
.abs{position:absolute}

/* hero */
.hero{left:0;top:0;width:1200px;height:779px;background:linear-gradient(180deg,#a9c9c9 0%,#8fae9e 35%,#6f8f6f 60%,#566b55 100%)}
.hero-figures{left:380px;top:60px;width:740px;height:719px;background:radial-gradient(ellipse at 30% 40%,#c9b3a3 0%,#8d8a9d 45%,rgba(90,80,140,0) 75%),radial-gradient(ellipse at 80% 45%,#8c79c9 0%,rgba(120,100,190,0) 60%)}
.nav-band{left:0;top:65px;width:1200px;height:32px;background:rgba(99,198,203,.85)}
.logo-box{left:40px;top:0;width:264px;height:188px;background:var(--white);border-radius:0 0 8px 8px;display:flex;flex-direction:column;align-items:center;justify-content:center;gap:10px}
.logo-mark{width:40px;height:40px;border-radius:50%;background:var(--teal)}
.logo-name{font-weight:700;font-size:22px;letter-spacing:2px;color:var(--teal-dark);text-align:center;line-height:1.1}
.nav{left:376px;top:65px;height:32px;display:flex;align-items:center;font-size:16px;color:var(--white)}
.nav a{color:var(--white);text-decoration:none;padding:0 18px;border-left:1px solid rgba(255,255,255,.8);line-height:16px}
.nav a:first-child{border-left:0;padding-left:0;color:var(--teal-dark)}
.btn-top{left:977px;top:57px;width:179px;height:44px;background:var(--teal-dark);color:var(--white);font-size:14px;font-weight:700;text-align:center;line-height:16px;padding-top:6px;border-radius:3px}
.hero-script{left:0;top:490px;width:1200px;text-align:center;font-family:"Great Vibes",cursive;font-size:92px;color:var(--white);text-shadow:0 2px 6px rgba(0,0,0,.35)}
.hero-sub{left:0;top:588px;width:1200px;text-align:center;font-size:50px;color:var(--white);text-shadow:0 2px 6px rgba(0,0,0,.35)}
.btn-hero{left:492px;top:662px;width:216px;height:44px;background:var(--teal-dark);color:var(--white);font-weight:700;font-size:16px;text-align:center;line-height:44px;border-radius:3px}

/* section headings */
.sec-title{left:0;width:1200px;text-align:center;font-weight:900;font-size:26px;color:var(--teal-head)}
.rule{height:2px;background:linear-gradient(90deg,rgba(79,193,198,0),var(--teal),rgba(79,193,198,0))}

/* about */
.about-photo{left:136px;top:931px;width:429px;height:227px;background:linear-gradient(135deg,#a8c86a 0%,#d9b28f 40%,#e8967c 65%,#8fb159 100%);border:6px solid var(--white);box-shadow:0 6px 14px rgba(0,0,0,.35)}
.about-text{left:629px;top:930px;width:425px;font-size:14.5px;line-height:20.5px;color:var(--ink-soft);text-align:justify}
.btn-pill{height:33px;border-radius:17px;font-size:11px;font-weight:700;text-align:center;line-height:33px;letter-spacing:.5px}
.btn-about{left:528px;top:1218px;width:152px;background:var(--teal);color:var(--white)}

/* emdr */
.emdr{left:0;top:1319px;width:1200px;height:334px;background:linear-gradient(90deg,#b08c6c 0%,#b79679 45%,#c7ad95 70%,#a88a72 100%)}
.emdr-eye{left:640px;top:1319px;width:560px;height:334px;background:radial-gradient(ellipse at 55% 50%,#6c5a4a 0%,#9f8470 22%,rgba(200,175,150,0) 60%)}
.emdr-title{color:var(--white)}
.emdr-text{left:110px;top:1442px;width:980px;text-align:center;font-size:14px;line-height:20px;color:var(--white)}
.btn-emdr{left:520px;top:1570px;width:148px;background:var(--white);color:var(--brown)}

/* services */
.services{left:0;top:1653px;width:1200px;height:553px;background:var(--teal-pale)}
.hub{left:508px;top:1864px;width:190px;height:190px;border-radius:50%;background:var(--white)}
.svc{width:230px;text-align:center}
.svc h3{font-size:14px;font-weight:900;color:var(--teal-head)}
.svc p{font-size:11.5px;font-weight:700;line-height:15px;color:var(--ink-soft);margin-top:3px}

/* testimonials */
.testi-title{left:117px;top:2306px;font-weight:900;font-size:26px;color:var(--teal-head)}
.arrow{width:20px;height:20px;border-radius:50%;background:var(--teal)}
.avatar{left:113px;top:2406px;width:158px;height:158px;border-radius:50%;background:radial-gradient(circle at 50% 45%,#f0d2bd 0%,#c97a4f 55%,#8c4a2a 100%);border:3px solid var(--white);box-shadow:0 0 0 1px #ccc}
.testi-name{left:113px;top:2585px;width:158px;text-align:center;font-weight:900;font-size:14px;color:var(--teal-head)}
.quote-mark{font-family:Georgia,serif;font-size:40px;color:var(--teal);line-height:1;font-weight:700}
.testi-text{left:298px;top:2418px;width:320px;font-size:13.5px;line-height:19px;color:var(--ink);text-align:justify;text-indent:22px}

/* form */
.form-box{left:702px;top:2311px;width:413px;height:300px;border:2px solid #b7d9db}
.form-tab{left:735px;top:2299px;width:344px;height:45px;background:var(--teal);color:var(--white);font-weight:700;font-size:20px;line-height:45px;text-align:center}
.field{left:737px;width:344px;background:#dcefef;border:1.5px solid var(--teal);border-radius:3px;font-size:17px;color:var(--ink-soft);padding:7px 18px}
.field sup{color:#e07070;font-size:11px}
.btn-submit{left:834px;top:2554px;width:140px;height:35px;border-radius:18px;background:var(--teal);color:var(--white);font-weight:700;font-size:15px;text-align:center;line-height:35px}

/* footer */
.footer{left:0;top:2700px;width:1200px;height:275px;background:var(--footer);color:var(--white)}
.foot-logo{left:73px;top:2778px;width:158px;display:flex;flex-direction:column;align-items:center;gap:8px}
.foot-logo .logo-mark{background:var(--white);width:34px;height:34px}
.foot-logo .logo-name{color:var(--white);font-size:18px}
.foot-about{left:73px;top:2860px;width:270px;font-size:11.5px;line-height:15px}
.vline{width:1px;background:rgba(255,255,255,.7);top:2745px;height:190px}
.foot-h{font-weight:700;font-size:19px;letter-spacing:.5px}
.foot-sep{height:1px;background:rgba(255,255,255,.7)}
.links{left:435px;top:2795px;list-style:none;font-size:15.5px;line-height:23.5px}
.links li::before{content:"‹";margin-right:14px}
.contact{left:678px;top:2812px;font-size:12.5px;line-height:22px}
.contact div{display:flex;align-items:center;gap:8px}
.contact svg{width:11px;height:11px}
.socials{left:960px;top:2803px;display:flex;gap:5px}
.socials span{width:24px;height:24px;border-radius:50%;background:var(--white)}
.call{left:958px;top:2883px;font-weight:700;font-size:21px;line-height:27px}
.bottom{left:0;top:2975px;width:1200px;height:60px;background:var(--footer-dark);color:#e4e4e4;text-align:center;line-height:60px;font-size:15px}
</style>
</head>
<body>

<!-- hero -->
<div class="abs hero" role="img" aria-label="Photo of a mother and daughter smiling by a wooden fence outdoors"></div>
<div class="abs hero-figures" aria-hidden="true"></div>
<div class="abs nav-band"></div>
<div class="abs logo-box"><span class="logo-mark"></span><span class="logo-name">WILLOWMERE<br>FAMILY COUNSELING</span></div>
<nav class="abs nav"><a>Home</a><a>About me</a><a>Services</a><a>EMDR</a><a>Insurance</a><a>Contact</a></nav>
<div class="abs btn-top">SCHEDULE YOUR<br>APPOINTMENT</div>
<div class="abs hero-script">Family Counseling Sessions</div>
<div class="abs hero-sub">Work With Me</div>
<div class="abs btn-hero">MAKE APPOINTMENT</div>

<!-- about -->
<h2 class="abs sec-title" style="top:838px">ABOUT ME</h2>
<div class="abs rule" style="left:470px;top:896px;width:260px"></div>
<div class="abs about-photo" role="img" aria-label="Photo of a smiling family of four outdoors"></div>
<p class="abs about-text">Lorem ipsum dolor sit amet, consectetuer adipiscing elit. Aenean commodo ligula eget dolor. Aenean massa. Cum sociis natoque penatibus et magnis dis parturient montes, nascetur ridiculus mus. Donec quam felis, ultricies nec, pellentesque eu, pretium quis, sem. Nulla consequat massa quis enim.Donec pede justo, fringilla vel, aliquet nec, vulputate eget, arcu. In enim justo, rhoncus ut, imperdiet a, venenatis vitae, justo. Nullam dictum felis eupede mollis pretium. Integer tincidunt. Cras dapibus. Vivamus elementum semper nisi. Aenean vulputate eleifend tellus. Aenean leo ligula, porttitor eu,blandit vel Cras dapibus. Vivamus elementum semper nisi.</p>
<div class="abs btn-pill btn-about">READ MORE</div>

<!-- emdr -->
<div class="abs emdr"></div>
<div class="abs emdr-eye" role="img" aria-label="Close-up photo of a human eye"></div>
<h2 class="abs sec-title emdr-title" style="top:1362px">EMDR</h2>
<div class="abs rule" style="left:520px;top:1418px;width:160px;background:linear-gradient(90deg,rgba(255,255,255,0),#fff,rgba(255,255,255,0))"></div>
<p class="abs emdr-text">Lorem ipsum dolor sit amet, consectetur adipiscing elit. Quid autem habent admirationis, cum prope accesseris? An hoc usque quaque, aliter in vita? Non igitur de improbo, sed de callido improbo quaerimus, qualis Q. Nam quibus rebus efficiuntur voluptates, eae non sunt in potestate sapientis. Negare non possum. Huic mori optimum esse propter desperationem sapientiae, illi propter spem vivere. Lorem ipsum dolor sit amet, consectetur adipiscing elit. Quid autem habent admirationis, cum prope accesseris? An hoc usque quaque, aliter in vita?<br>Non igitur de improbo, sed de callido improbo quaerimus, qualis Q.</p>
<div class="abs btn-pill btn-emdr">READ MORE</div>

<!-- services -->
<div class="abs services"></div>
<h2 class="abs sec-title" style="top:1704px">SERVICES</h2>
<div class="abs rule" style="left:470px;top:1762px;width:260px"></div>
<svg class="abs" style="left:0;top:1653px" width="1200" height="553" viewBox="0 1653 1200 553" aria-hidden="true">
  <g stroke="#2ea7ae" stroke-width="2">
    <line x1="420" y1="1855" x2="505" y2="1900"/>
    <line x1="418" y1="1973" x2="490" y2="1973"/>
    <line x1="420" y1="2085" x2="505" y2="2030"/>
    <line x1="780" y1="1855" x2="695" y2="1900"/>
    <line x1="782" y1="1973" x2="712" y2="1973"/>
    <line x1="780" y1="2085" x2="695" y2="2030"/>
  </g>
</svg>
<div class="abs hub"></div>
<div class="abs svc" style="left:233px;top:1800px"><h3>LOREM IPSUM</h3><p>Lorem ipsum dolor sit amet,<br>consectetur adipiscing</p></div>
<div class="abs svc" style="left:181px;top:1943px"><h3>LOREM IPSUM</h3><p>Lorem ipsum dolor sit amet,<br>consectetur adipiscing</p></div>
<div class="abs svc" style="left:233px;top:2090px"><h3>LOREM IPSUM</h3><p>Lorem ipsum dolor sit amet,<br>consectetur adipiscing</p></div>
<div class="abs svc" style="left:737px;top:1800px"><h3>LOREM IPSUM</h3><p>Lorem ipsum dolor sit amet,<br>consectetur adipiscing</p></div>
<div class="abs svc" style="left:789px;top:1943px"><h3>LOREM IPSUM</h3><p>Lorem ipsum dolor sit amet,<br>consectetur adipiscing</p></div>
<div class="abs svc" style="left:737px;top:2090px"><h3>LOREM IPSUM</h3><p>Lorem ipsum dolor sit amet,<br>consectetur adipiscing</p></div>

<!-- testimonials -->
<h2 class="abs testi-title">TESTIMONIALS</h2>
<div class="abs rule" style="left:117px;top:2360px;width:500px;background:linear-gradient(90deg,var(--teal),rgba(79,193,198,0))"></div>
<svg class="abs" style="left:566px;top:2312px" width="50" height="22" viewBox="0 0 50 22" aria-hidden="true">
  <circle cx="11" cy="11" r="10" fill="#4fc1c6"/><path d="M13 6l-5 5 5 5" stroke="#fff" stroke-width="2.5" fill="none"/>
  <circle cx="38" cy="11" r="10" fill="#4fc1c6"/><path d="M36 6l5 5-5 5" stroke="#fff" stroke-width="2.5" fill="none"/>
</svg>
<div class="abs avatar" role="img" aria-label="Portrait photo of a client with red hair"></div>
<div class="abs testi-name">CLARA</div>
<div class="abs quote-mark" style="left:296px;top:2410px">“</div>
<p class="abs testi-text">Lorem ipsum dolor sit amet, consectetur adipiscing elit. Quid autem habent admirationis, cum prope accesseris? An hoc usque quaque, aliter in vita? Non igitur de improbo, sed de callido improbo quaerimus, qualis Q. Nam quibus rebus efficiuntur voluptates, eae non sunt in potestate sapientis. Negare non possum.</p>
<div class="abs quote-mark" style="left:428px;top:2537px">”</div>

<div class="abs form-box"></div>
<div class="abs form-tab">SCHEDULE YOUR APPOINTMENT</div>
<div class="abs field" style="top:2362px;height:38px">Name<sup>*</sup></div>
<div class="abs field" style="top:2408px;height:39px">Email<sup>*</sup></div>
<div class="abs field" style="top:2455px;height:83px">Message<sup>*</sup></div>
<div class="abs btn-submit">SUBMIT</div>

<!-- footer -->
<div class="abs footer"></div>
<div class="abs foot-logo"><span class="logo-mark"></span><span class="logo-name">WILLOWMERE</span></div>
<p class="abs foot-about">Lorem ipsum dolor sit amet, consectetur adipiscing elit. Quid autem habent admirationis, cum prope accesseris? An hoc usque quaque, aliter in vita? Non igitur de improbo.</p>
<div class="abs vline" style="left:385px"></div>
<div class="abs vline" style="left:621px"></div>
<div class="abs vline" style="left:921px"></div>

<div class="abs foot-h" style="left:435px;top:2743px">QUICK LINKS</div>
<div class="abs foot-sep" style="left:435px;top:2778px;width:150px"></div>
<ul class="abs links"><li>Home</li><li>About me</li><li>Services</li><li>EMDR</li><li>Insurance</li><li>Contact</li></ul>

<div class="abs foot-h" style="left:678px;top:2743px">CONTACT</div>
<div class="abs foot-sep" style="left:678px;top:2778px;width:180px"></div>
<div class="abs contact">
  <div style="line-height:17px;margin-bottom:4px">742 Linden Park Rd<br>Maple Falls, OR 97301</div>
  <div><svg viewBox="0 0 12 12"><path d="M2 1l3 1-1 2 4 4 2-1 1 3-2 1C5 11 1 7 1 3z" fill="#fff"/></svg>555-201-4830</div>
  <div><svg viewBox="0 0 12 12"><rect x="3" y="0.5" width="6" height="11" rx="1" fill="none" stroke="#fff"/></svg>555-201-7716</div>
  <div><svg viewBox="0 0 12 12"><rect x="0.5" y="2" width="11" height="8" fill="#fff"/><path d="M1 2.5l5 4 5-4" stroke="#a7a7a7" fill="none"/></svg>hello@willowmere.com</div>
  <div><svg viewBox="0 0 12 12"><circle cx="6" cy="6" r="5.3" fill="none" stroke="#fff"/><path d="M1 6h10M6 1c-3 3-3 7 0 10M6 1c3 3 3 7 0 10" stroke="#fff" fill="none" stroke-width=".8"/></svg>www.willowmere.com</div>
</div>

<div class="abs foot-h" style="left:955px;top:2743px">FOLLOW US ON</div>
<div class="abs socials"><span></span><span></span><span></span><span></span><span></span></div>
<div class="abs foot-sep" style="left:960px;top:2862px;width:40px"></div>
<div class="abs call">CALL US ON<br>555-201-4830</div>

<div class="abs bottom">© 2018 Willowmere &nbsp;|&nbsp; Privacy Policy &nbsp;|&nbsp; User Agreement</div>

</body>
</html>
```